Coffee bag stamp design for new coffee brand

Stamp design that will be used like a label on a coffee package.
It must be a vector that can be produced as a stamp. Coffee bag is from brown craft paper. I upload image of this bag. Size of design is 80mm x 140mm.
I also uploaded two pictures for inspiration, but I will also appreciate new ideas.

Target Market(s)

Coffee lovers, who love to try new coffee. Also hipsters.

Colors

Designer to choose only greyscale colors for use in the design.

Requirements
Must have
• Some information about coffee must have:
Name: BRAZIL (the biggest font in that design)
Region: Santos
Altitude: 60 – 1200 m.n.m.
Variety: Arabica
Processing: unwashed

```html
<!DOCTYPE html>
<html lang="en">
<head>
<meta charset="utf-8">
<title>Kestrel Coffee – Brazil bag stamp</title>
<link rel="stylesheet" href="https://fonts.googleapis.com/css2?family=Josefin+Sans:wght@700&family=Arvo:ital,wght@0,700;1,400&display=swap">
<style>
  :root{
    --backdrop:#e1e2e1;
    --kraft:#c4a47c;
    --ink:#111111;
    --paper-black:#000000;
    --white:#ffffff;
    --foliage:#6f8d88;
    --foliage-deep:#5a7a75;
    --accent:#f2ec1c;
  }
  *{margin:0;padding:0;box-sizing:border-box}
  html,body{width:1200px;height:1200px;overflow:hidden;background:var(--backdrop)}
  .canvas{position:relative;width:1200px;height:1200px}
  .stamp{position:absolute;width:342px;height:596px;overflow:hidden}
  .stamp--kraft{left:40px;top:255px;background:var(--kraft);color:var(--ink)}
  .stamp--black{left:440px;top:261px;background:var(--paper-black);color:var(--white)}
  .stamp--diamond{left:822px;top:262px;background:var(--kraft);color:var(--ink)}

  .ornament{position:absolute;
    background:radial-gradient(closest-side,var(--foliage) 0%,var(--foliage-deep) 55%,rgba(90,122,117,0) 100%);
    opacity:.85}
  .stamp--kraft .ornament{left:8px;top:70px;width:316px;height:336px}
  .stamp--black .ornament{left:16px;top:64px;width:310px;height:332px}

  .brand{position:absolute;left:0;width:100%;text-align:center;
    font-family:"Josefin Sans",sans-serif;font-weight:700;font-size:31px;line-height:29px;letter-spacing:1px}
  .stamp--kraft .brand{top:156px}
  .stamp--black .brand{top:150px}

  .rule{position:absolute;background:currentColor}
  .origin{position:absolute;left:0;width:100%;text-align:center;
    font-family:"Josefin Sans",sans-serif;font-weight:700;font-size:30px;letter-spacing:2px;line-height:30px}
  .spec{position:absolute;width:150px;text-align:center}
  .spec__label{display:block;font-family:Arvo,serif;font-style:italic;font-size:11px;letter-spacing:1px;line-height:13px}
  .spec__value{display:block;font-family:"Josefin Sans",sans-serif;font-weight:700;font-size:18px;letter-spacing:1px;line-height:20px}

  .diamond svg{display:block}
  .diamond text{font-family:"Josefin Sans",sans-serif;font-weight:700;fill:var(--ink);text-anchor:middle}
  .diamond .lbl{font-family:Arvo,serif;font-style:italic;font-weight:400;font-size:6px}
</style>
</head>
<body>
<main class="canvas">

  <section class="stamp stamp--kraft">
    <div class="ornament" role="img" aria-label="Swirling leaf ornament in grey-green with yellow petal accents"></div>
    <h1 class="brand">KESTREL<br>COFFEE</h1>
    <div class="rule" style="left:15px;top:409px;width:297px;height:4px"></div>
    <h2 class="origin" style="top:418px">BRAZIL</h2>
    <div class="rule" style="left:15px;top:446px;width:297px;height:4px"></div>
    <div class="rule" style="left:15px;top:488px;width:297px;height:2px"></div>
    <div class="rule" style="left:162px;top:448px;width:3px;height:83px"></div>
    <div class="spec" style="left:15px;top:455px"><span class="spec__label">REGION</span><span class="spec__value">SANTOS</span></div>
    <div class="spec" style="left:168px;top:455px"><span class="spec__label">ALTITUDE</span><span class="spec__value">60–1200<small>M.N.M</small></span></div>
    <div class="spec" style="left:15px;top:496px"><span class="spec__label">PROCESSING</span><span class="spec__value">UNWASHED</span></div>
    <div class="spec" style="left:168px;top:496px"><span class="spec__label">VARIETY</span><span class="spec__value">ARABICA</span></div>
  </section>

  <section class="stamp stamp--black">
    <div class="ornament" role="img" aria-label="Swirling leaf ornament in grey-green with yellow petal accents"></div>
    <h1 class="brand">KESTREL<br>COFFEE</h1>
    <div class="rule" style="left:18px;top:401px;width:297px;height:1px"></div>
    <h2 class="origin" style="top:408px">BRAZIL</h2>
    <div class="rule" style="left:18px;top:437px;width:297px;height:1px"></div>
    <div class="rule" style="left:18px;top:476px;width:297px;height:1px"></div>
    <div class="rule" style="left:166px;top:438px;width:1px;height:81px"></div>
    <div class="spec" style="left:18px;top:444px"><span class="spec__label">REGION</span><span class="spec__value">SANTOS</span></div>
    <div class="spec" style="left:168px;top:444px"><span class="spec__label">ALTITUDE</span><span class="spec__value">60–1200<small>M.N.M</small></span></div>
    <div class="spec" style="left:18px;top:484px"><span class="spec__label">PROCESSING</span><span class="spec__value">UNWASHED</span></div>
    <div class="spec" style="left:168px;top:484px"><span class="spec__label">VARIETY</span><span class="spec__value">ARABICA</span></div>
  </section>

  <section class="stamp stamp--diamond diamond">
    <svg width="342" height="596" viewBox="0 0 342 596" aria-label="Kestrel Coffee Brazil diamond stamp">
      <defs>
        <clipPath id="inner-diamond"><polygon points="171,165 305,308 171,451 37,308"/></clipPath>
      </defs>
      <polygon points="171,154 318,308 171,462 24,308" fill="none" stroke="#111" stroke-width="3"/>
      <polygon points="171,165 305,308 171,451 37,308" fill="none" stroke="#111" stroke-width="1.5"/>
      <g clip-path="url(#inner-diamond)" stroke="#111">
        <line x1="0" y1="232" x2="342" y2="232" stroke-width="1.5"/>
        <line x1="0" y1="280" x2="342" y2="280" stroke-width="3"/>
        <line x1="115" y1="280" x2="115" y2="320" stroke-width="1.5"/>
        <line x1="207" y1="280" x2="207" y2="320" stroke-width="1.5"/>
        <line x1="0" y1="320" x2="342" y2="320" stroke-width="3"/>
        <line x1="0" y1="352" x2="342" y2="352" stroke-width="1.5"/>
        <line x1="168" y1="352" x2="168" y2="386" stroke-width="1.5"/>
        <line x1="0" y1="386" x2="342" y2="386" stroke-width="1.5"/>
      </g>
      <text x="171" y="214" font-size="9">KESTREL</text>
      <text x="171" y="224" font-size="9">COFFEE</text>
      <text x="171" y="272" font-size="17" letter-spacing="1">BRAZIL</text>
      <text class="lbl" x="86" y="295">REGION</text>
      <text x="86" y="308" font-size="8">SANTOS</text>
      <text class="lbl" x="161" y="295">VARIETY</text>
      <text x="161" y="308" font-size="8">ARABICA</text>
      <text class="lbl" x="240" y="295">ALTITUDE</text>
      <text x="240" y="308" font-size="6">60-1200M.N.M</text>
      <text class="lbl" x="171" y="331">PROCESSING</text>
      <text x="171" y="345" font-size="12">UNWASHED</text>
      <text class="lbl" x="130" y="361">DATE</text>
      <text class="lbl" x="216" y="361">NET WT</text>
      <text x="171" y="398" font-size="7">YOUR</text>
      <text x="171" y="407" font-size="7">ROASTING</text>
      <text x="171" y="416" font-size="7">COMPANY</text>
    </svg>
  </section>

</main>
</body>
</html>
```